Optometric Practice needs Initial Photoshop Mockup

We need a graphic design for the homepage of a website for an optometric practice that specializes in vision therapy.

Here's the link to the project folder on Stashly. I've included photos, example sites, content and instructions.

https://www.stashly-files.example/sh/k2wq8rn5tz1xv3m/BQX_LmRtYpeKa7NzHdVcWUbQo

Please feel free to submit any questions about the design. I'll be happy to help guide you in any areas you're uncertain of.

Okay - I've updated the project to payment confirmed. Let's see some designs :) Thanks, Reg

```html
<!DOCTYPE html>
<html lang="en">
<head>
<meta charset="utf-8">
<title>VisionBridge Learning Centers – Home</title>
<link href="https://fonts.googleapis.com/css2?family=Open+Sans:wght@400;600;700&display=swap" rel="stylesheet">
<style>
:root{
  --red:#b30f0f;
  --red-dark:#8f0a0a;
  --navy:#141b6b;
  --blue-btn:#2b2fc0;
  --ink:#333;
  --muted:#777;
  --rule:#dcdcdc;
  --sky:#dcecf3;
  --footer:#333333;
  --footer-base:#262626;
  --panel:#f1f1f1;
}
*{box-sizing:border-box;margin:0;padding:0}
html,body{width:794px;height:1200px;overflow:hidden;background:#fff}
body{font-family:"Open Sans",Arial,sans-serif;color:var(--ink);position:relative}
a{text-decoration:none;color:inherit}
.abs{position:absolute}
.top-rule{left:0;top:0;width:794px;height:3px;background:var(--red)}
.brand{left:66px;top:30px;width:130px;height:50px;display:flex;align-items:center;gap:6px}
.brand-mark{width:12px;height:12px;border-radius:50%;background:var(--red)}
.brand-name{font-size:28px;font-weight:700;color:var(--red);letter-spacing:1px}
.brand-sep{left:203px;top:14px;width:1px;height:70px;background:linear-gradient(#fff,#ddd,#fff)}
.tagline{left:211px;top:31px;font-size:8px;line-height:13px;color:#333}
.call{right:66px;top:30px;font-size:10.5px;color:#333}
.appt{left:575px;top:49px;width:153px;height:21px;background:var(--blue-btn);color:#fff;font-size:10px;display:flex;align-items:center;justify-content:center}
.sky{left:0;top:110px;width:794px;height:300px;background:linear-gradient(var(--sky),#f4f9fb 70%,#fff)}
.nav{left:66px;top:95px;width:662px;height:27px;background:#fff;border:1px solid #e3e3e3;display:flex;align-items:center;padding:0 3px}
.nav a{font-size:8px;color:#888;padding:0 10px;height:19px;display:flex;align-items:center;border-right:1px solid #e6e6e6}
.nav a.active{color:var(--red);background:#f3f3f3}
.nav a:last-child{border-right:none}
.hero{left:66px;top:162px;width:487px;height:202px;background:linear-gradient(90deg,#ebe6df,#f1efe9 55%,#e6ebe4);overflow:hidden}
.hero-photo{left:4px;top:4px;width:175px;height:198px;background:linear-gradient(160deg,#c9a47a,#7fc3dd 60%,#e8e3da)}
.hero-text{left:190px;top:46px}
.hero-title{font-size:20px;color:var(--red);font-weight:400;line-height:1}
.hero-title b{font-size:36px;font-weight:700}
.hero-sub{font-size:12px;color:var(--red);margin-top:2px}
.hero-copy{font-size:8px;line-height:11px;color:#555;width:270px;margin-top:9px}
.hero-btn{margin-top:9px;width:110px;height:20px;background:var(--navy);color:#fff;font-size:9.5px;display:flex;align-items:center;justify-content:center}
.dots{left:255px;top:374px;display:flex;gap:6px}
.dots i{width:7px;height:7px;border-radius:50%;border:1.5px solid #bbb;background:#fff;display:block}
.cats{left:553px;top:146px;width:175px;height:237px;background:linear-gradient(90deg,var(--red),#c41616);color:#fff}
.cats-notch{left:540px;top:146px;width:0;height:0;border-top:14px solid transparent;border-right:13px solid var(--red-dark)}
.cats h2{font-size:15px;font-weight:600;padding:8px 13px 6px;height:34px;border-bottom:1px solid rgba(0,0,0,.15)}
.cats li{list-style:none;font-size:8px;height:33.8px;display:flex;align-items:center;padding-left:12px;border-bottom:1px solid rgba(0,0,0,.15);border-top:1px solid rgba(255,255,255,.08)}
.cats li:last-child{border-bottom:none}
.cats li span{margin-left:7px;font-weight:700}
.strip-rule{left:66px;top:402px;width:662px;height:1px;background:var(--rule)}
.strip-text{left:66px;top:407px;font-size:8px;color:#888}
.more-link{right:66px;top:407px;font-size:8px;color:#888;display:flex;align-items:center;gap:6px}
.more-link i{width:9px;height:9px;border-radius:50%;background:var(--red);display:flex;align-items:center;justify-content:center;color:#fff;font-size:6px;font-style:normal;font-weight:700}
.tile{top:431px;height:100px}
.play{left:50%;top:50%;width:34px;height:34px;margin:-17px 0 0 -17px;border-radius:50%;background:#d43a2a}
.about-h{left:66px;top:553px;font-size:14.5px;font-weight:400;color:var(--navy)}
.about-h b{font-weight:600}
.about-rule{left:66px;top:579px;width:471px;height:1px;background:var(--rule)}
.about-sub{left:66px;top:585px;font-size:7px;color:#888}
.about-sub span{color:#2a3ac0}
.share{top:588px;height:11px;border:1px solid #ccc;border-radius:2px;font-size:6.5px;font-weight:700;color:#3b5998;display:flex;align-items:center;padding:0 5px;background:#f7f7f7}
.doc-photo{left:66px;top:609px;width:128px;height:133px;background:linear-gradient(#e6e0d8,#c79a80 45%,#3a3a40)}
.about-copy{left:211px;top:607px;width:318px;font-size:7.5px;line-height:11.4px;color:#555}
.about-copy p+p{margin-top:11px}
.rm{font-size:8px;color:var(--red)}
.card-img{top:761px;height:81px}
.card-text{top:849px;width:152px;font-size:7.3px;line-height:10.6px;color:#666}
.card-rm{top:899px}
.stories{left:552px;top:559px;width:176px;height:201px;background:var(--panel);border:1px solid #e2e2e2}
.stories h3{background:var(--navy);color:#fff;font-size:13.5px;font-weight:400;height:31px;display:flex;align-items:center;padding-left:11px}
.story{padding:10px 11px 0;font-size:7px;line-height:12px;color:#888;border-bottom:1px solid #e0e0e0;height:85px}
.story:last-child{border-bottom:none}
.story cite{display:block;font-style:normal;color:var(--red);font-size:7.5px;margin-top:10px}
.stories-btn{left:552px;top:772px;width:176px;height:21px;background:var(--red);color:#fff;font-size:8.5px;font-weight:600;display:flex;align-items:center;justify-content:center}
.social{left:552px;top:806px;width:177px;height:161px;border:1px solid #b6c0d6;background:#fff}
.social-h{font-size:6.5px;font-weight:700;color:#333;padding:3px 4px;border-bottom:1px solid #e4e4e4}
.social-page{display:flex;gap:4px;padding:5px 5px 0}
.social-thumb{width:29px;height:29px;background:linear-gradient(#d6d0c8,#b08a74)}
.social-name{font-size:7px;font-weight:700;color:#3b5998;line-height:9px}
.like-btn{display:inline-block;margin-top:2px;background:#5f78ab;color:#fff;font-size:6px;font-weight:700;padding:1px 4px}
.social-count{font-size:5.5px;color:#666;padding:6px 5px 4px;line-height:7px;border-bottom:1px solid #eee}
.social-count span{color:#3b5998}
.fans{display:grid;grid-template-columns:repeat(5,29px);gap:3px;padding:5px}
.fans i{height:29px;display:block;background:#c9c4bd}
.footer{left:0;top:1000px;width:794px;height:174px;background:var(--footer);border-top:3px solid var(--red)}
.footer-brand{left:66px;top:1028px;display:flex;align-items:center;gap:7px}
.footer-brand .brand-mark{background:#fff}
.footer-brand .brand-name{color:#fff;font-size:30px}
.footer-brand-sub{left:69px;top:1068px;font-size:7.5px;color:#fff;line-height:9px}
.footer-blurb{left:66px;top:1113px;width:195px;font-size:7.5px;line-height:12px;color:#fff}
.fcol{top:1032px}
.fcol h4{font-size:9px;font-weight:700;color:#fff;letter-spacing:.8px;margin-bottom:8px}
.fcol li{list-style:none;font-size:9.5px;color:#ddd;letter-spacing:.5px;line-height:17.3px}
.fcol address{font-style:normal;font-size:7.7px;color:#ddd;line-height:13.2px}
.base{left:0;top:1174px;width:794px;height:26px;background:var(--footer-base);color:#fff;font-size:7.5px;display:flex;align-items:center;justify-content:center}
</style>
</head>
<body>
<div class="abs top-rule"></div>

<header>
  <a class="abs brand" href="#"><span class="brand-mark"></span><span class="brand-name">VBLC</span></a>
  <div class="abs brand-sep"></div>
  <div class="abs tagline">VisionBridge Learning Centers, Inc.<br>Dr. Daniel Marsh</div>
  <div class="abs call">Call Us for Help : 555-014-2290</div>
  <a class="abs appt" href="#">Request an Appointment</a>
</header>

<div class="abs sky"></div>

<nav class="abs nav">
  <a class="active" href="#">Home</a><a href="#">Meet Us</a><a href="#">New Patients</a><a href="#">Vision &amp; Learning</a><a href="#">Vision Therapy</a><a href="#">Binocular Vision Disorders</a><a href="#">Head Injuries</a><a href="#">Professionals</a><a href="#">Contact Us</a>
</nav>

<section class="abs hero">
  <div class="abs hero-photo" role="img" aria-label="Photo of a frustrated student reading a book at a desk"></div>
  <div class="abs hero-text">
    <h1 class="hero-title">Welcome to The <b>VBLC</b></h1>
    <div class="hero-sub">VisionBridge Learning Centers</div>
    <p class="hero-copy">Sed ut perspiciatis unde omnis iste natus error sit totam rem aperia eaque ipsa quae ab illo inventore veritatis et quasi architecto beatae vitae dicta sunt explicabo.</p>
    <a class="hero-btn" href="#">Read More</a>
  </div>
</section>
<div class="abs dots"><i></i><i></i><i></i><i></i><i></i><i></i><i></i><i></i></div>

<div class="abs cats-notch"></div>
<aside class="abs cats">
  <h2>Categories</h2>
  <ul>
    <li>Improving Vision<span>›</span></li>
    <li>Improving Vision Changing Lives<span>›</span></li>
    <li>Improving Changing Lives<span>›</span></li>
    <li>Improving Vision, Changing<span>›</span></li>
    <li>Improving Vision, Changing Lives<span>›</span></li>
    <li>Vision Changing Lives<span>›</span></li>
  </ul>
</aside>

<div class="abs strip-rule"></div>
<p class="abs strip-text">Lorem ipsum dolor sit amet elit, sed do ut labore et dolore magna aliqua.</p>
<a class="abs more-link" href="#">Read More <i>›</i></a>

<div class="abs tile" style="left:66px;width:227px;background:linear-gradient(120deg,#d8d2c4,#8a7560 50%,#e9e6df)" role="img" aria-label="Photo of a woman reading papers at a desk"></div>
<div class="abs tile" style="left:310px;width:227px;background:linear-gradient(120deg,#6b5a4c,#a79985 50%,#5a5048)" role="img" aria-label="Video still of a child writing in class">
  <span class="abs play"></span>
  <svg class="abs" style="left:108px;top:43px" width="14" height="14" viewBox="0 0 14 14"><path d="M2 1 L13 7 L2 13Z" fill="#fff"/></svg>
</div>
<div class="abs tile" style="left:553px;width:175px;background:linear-gradient(#7d8a57,#b8946a 55%,#c6a57b)" role="img" aria-label="Photo of a baseball batter and catcher at home plate"></div>

<h2 class="abs about-h">About <b>VisionBridge Learning Centers</b></h2>
<div class="abs about-rule"></div>
<p class="abs about-sub">Lorem ipsum <span>dolor sit amet elit,</span> sed do ut magna aliqua.</p>
<span class="abs share" style="left:459px">Share</span>
<span class="abs share" style="left:503px">Like</span>

<div class="abs doc-photo" role="img" aria-label="Portrait photo of the doctor"></div>
<div class="abs about-copy">
  <p>There are many visual skills critical for reading and learning. Often, a vision problem is misdiagnosed as an attention problem or a learning disability due to similarity of symptoms. Anyone who is struggling with reading, has poor reading comprehension, or just isn't performing to their full potential, should consider scheduling a developmental vision evaluation. To help determine if you or your child should be tested, Do the Check-list on our Vision Quiz page.</p>
  <p>Dr. Daniel Marsh is a developmental optometrist who specializes in the diagnosis and treatment of vision problems that interfere with reading and learning. He is a member of the National Vision Care Society, the Guild of Developmental Optometry .</p>
</div>
<a class="abs rm" style="left:212px;top:734px" href="#">Read More &nbsp;»</a>

<div class="abs card-img" style="left:66px;width:153px;background:linear-gradient(120deg,#c9a48c,#d9c6c0 50%,#8c8c8c)" role="img" aria-label="Photo of a mother helping a daughter with homework"></div>
<div class="abs card-img" style="left:226px;width:152px;background:linear-gradient(120deg,#d08a2c,#e7c08f 50%,#c07a28)" role="img" aria-label="Photo of a smiling girl holding a book"></div>
<div class="abs card-img" style="left:385px;width:152px;background:linear-gradient(120deg,#c48a3a,#ddd2c4 50%,#3f3f3f)" role="img" aria-label="Photo of a child at an eye examination instrument"></div>
<p class="abs card-text" style="left:66px">Sed ut perspiciatis unde omnis iste natus error sit totam rem aperiam, eaque ipsa quae ab illo inventore veritatis et quasi architecto beatae</p>
<p class="abs card-text" style="left:224px">Sed ut perspiciatis unde omnis iste natus error sit totam rem aperiam, eaque ipsa quae ab illo inventore veritatis et quasi architecto beatae</p>
<p class="abs card-text" style="left:384px">Sed ut perspiciatis unde omnis iste natus error sit totam rem aperiam, eaque ipsa quae ab illo inventore veritatis et quasi architecto beatae</p>
<a class="abs rm card-rm" style="left:66px" href="#">Read More &nbsp;»</a>
<a class="abs rm card-rm" style="left:224px" href="#">Read More &nbsp;»</a>
<a class="abs rm card-rm" style="left:384px" href="#">Read More &nbsp;»</a>

<aside class="abs stories">
  <h3>Success Stories</h3>
  <div class="story">J. is a happier child who is more in control of his body and movements. School work is much less of a struggle, and he is enjoying learning.<cite>J.B., Child's Age 8</cite></div>
  <div class="story">I want to thank you for all your help and encouragement, which has restored my confidence.<cite>R.R., Adult Brain Injury Patient</cite></div>
</aside>
<a class="abs stories-btn" href="#">View More Stories</a>

<aside class="abs social">
  <div class="social-h">Find us on Friendlink</div>
  <div class="social-page">
    <div class="social-thumb" role="img" aria-label="Small portrait of the doctor"></div>
    <div><div class="social-name">VBLC: Dr. Daniel Marsh,<br>Developmental Optometrist</div><span class="like-btn">Like</span></div>
  </div>
  <p class="social-count">155 people like <span>VBLC: Dr. Daniel Marsh, Developmental Optometrist.</span></p>
  <div class="fans" role="img" aria-label="Grid of follower profile pictures">
    <i></i><i></i><i></i><i></i><i style="background:#e4e4e4"></i><i style="background:#e07a2c"></i><i></i><i></i><i></i><i></i>
  </div>
</aside>

<footer>
  <div class="abs footer"></div>
  <div class="abs footer-brand"><span class="brand-mark"></span><span class="brand-name">VBLC</span></div>
  <div class="abs footer-brand-sub">The VisionBridge Learning<br>Centers, Inc.</div>
  <p class="abs footer-blurb">Sed ut perspiciatis unde omnis iste natus error sit voluptatem accusantium doloremque laudantium totam rem aperiam, sunt explicabo.</p>
  <div class="abs fcol" style="left:307px"><h4>ABOUT US</h4><ul><li>About VBLC</li><li>Company</li><li>T&amp;C</li><li>Privacy</li><li>Press</li></ul></div>
  <div class="abs fcol" style="left:435px"><h4>COMMUNITY</h4><ul><li>Blog</li><li>Support</li><li>Translation Tool</li><li>Developer</li></ul></div>
  <div class="abs fcol" style="left:560px"><h4>CONTACT US</h4><address>Dr. Daniel Marsh<br>412 Harbor Ridge Way Riverside Center<br>Ste. 3<br>Maplewood, ST 00000 Phone: 555-014-2290<br>Fax: 555-014-2291</address></div>
  <div class="abs base">Copyrights © 2014 VBLC.example - All Rights Reserved</div>
</footer>
</body>
</html>
```